Home page design for a business selling commercial cleaning machines

We need a home page web design for a wholesale business selling commercial and industrial cleaning machines and spare parts. There is a huge range of products but we don't want the home page to be too cluttered and confusing.
- The design needs to be practical and functional - sharp corners, lots of white with just accents/splashes of the business colours.
- This is a link to their holding page which is very very basic - http://www.vornaspec.co.nz/ - use this to get the accent colours but please use lots and lots more WHITE in the home page design! There are no colour codes available.
- The attached HPID (home page design information) is in table boxes just to see placement of information. Information in orange text. Words to go on the design in black text.
- Expected standard of design examples:
http://brimalo-aquaforce.com/
http://brimalointernational.com/
http://tovesk.com/
http://www.mulfin.wb.gs/ (different industry)
- Only use Google fonts. Non-responsive. Width 1100pixels. Header height (without nav bar) 150-160 pixels.
- Will need a PSD of the chosen homepage design (CS5 compatible)

```html
<!DOCTYPE html>
<html lang="en">
<head>
<meta charset="utf-8">
<title>Vornaspec – Commercial Cleaning Machines</title>
<link href="https://fonts.googleapis.com/css2?family=Oswald:wght@400;600&family=Open+Sans:wght@400;600;700&display=swap" rel="stylesheet">
<style>
:root{
  --navy:#1d2944;
  --navy-deep:#141d31;
  --blue:#2b5d9c;
  --sky:#dfe8f2;
  --grey:#e9e9e9;
  --mid:#8a8a8a;
  --text:#333;
  --yellow:#f5d21b;
  --red:#c8262b;
  --white:#fff;
}
*{box-sizing:border-box;margin:0;padding:0}
html,body{width:667px;height:1200px;overflow:hidden;background:var(--white)}
body{font-family:"Open Sans",Arial,sans-serif;color:var(--text);font-size:7px;position:relative}
.header{height:67px;background:linear-gradient(#f6f9fc,var(--sky));display:flex;align-items:center;padding:0 15px;justify-content:space-between}
.brand{font-family:"Oswald",sans-serif;font-weight:600;font-size:24px;color:var(--navy);display:flex;align-items:center;gap:6px}
.brand i{width:10px;height:10px;background:var(--blue);display:block}
.tagline{width:210px;color:var(--blue);font-weight:600;font-size:7px;line-height:1.35;text-align:center;border-left:1px solid #b9c6d6;border-right:1px solid #b9c6d6;padding:0 8px}
.contact{text-align:right;color:var(--navy);font-size:6px;line-height:1.4}
.phone{font-family:"Oswald",sans-serif;font-size:20px;display:flex;align-items:center;justify-content:flex-end;gap:5px;margin-top:2px}
.nav{height:22px;background:var(--navy);display:flex;padding:0 15px}
.nav a{color:#dfe5ee;text-decoration:none;font-size:6.5px;padding:0 8px;line-height:22px}
.nav a.active{background:var(--blue);color:#fff}
.hero{position:absolute;top:92px;left:15px;width:630px;height:230px;display:flex}
.hero-photo{width:362px;position:relative;background:radial-gradient(ellipse 90px 110px at 62% 62%,#b8403a 0%,rgba(184,64,58,.55) 45%,rgba(184,64,58,0) 100%),linear-gradient(120deg,#d8d2c6 0%,#a79d8f 40%,#6d6761 75%,#c9c3b8 100%)}
.hero-photo .caption{position:absolute;left:150px;bottom:26px;font-family:"Oswald",sans-serif;font-weight:600;font-size:15px;color:var(--yellow);letter-spacing:.5px;text-shadow:0 1px 2px rgba(0,0,0,.5)}
.dots{position:absolute;bottom:10px;left:0;right:0;display:flex;justify-content:center;gap:4px}
.dots i{width:5px;height:5px;border-radius:50%;background:#fff;opacity:.6}
.dots i:first-child{opacity:1}
.why{flex:1;background:var(--navy-deep);color:#e3e8f0;padding:12px 14px}
.why h2{font-family:"Oswald",sans-serif;font-weight:400;font-size:13px;color:#fff;margin-bottom:8px;border-bottom:1px solid #3a4660;padding-bottom:6px}
.why li{list-style:none;font-size:7px;line-height:1.75;margin-bottom:3px;padding-left:10px;position:relative}
.why li:before{content:"";position:absolute;left:0;top:5px;width:4px;height:4px;background:var(--blue)}
.section-title{position:absolute;top:340px;left:15px;width:637px;height:22px;border-bottom:2px solid var(--navy)}
.section-title span{display:inline-block;background:var(--navy);color:#fff;font-family:"Oswald",sans-serif;font-size:11px;line-height:22px;padding:0 12px}
.products{position:absolute;top:374px;left:15px;width:637px;height:108px;display:flex;align-items:center;justify-content:space-between}
.arrow{width:14px;font-size:18px;color:var(--mid);text-align:center}
.product{width:108px;text-align:center}
.product .pic{height:78px;width:80px;margin:0 auto 6px;background:radial-gradient(ellipse 30px 34px at 50% 55%,#3d5f8f 0%,#7d8fa8 45%,#d9dee5 80%,#fff 100%)}
.product span{font-family:"Oswald",sans-serif;font-weight:600;font-size:7px;color:var(--navy)}
.browse{position:absolute;top:500px;left:15px;width:637px;height:45px;background:var(--grey);display:flex;align-items:center}
.browse-tab{height:45px;width:80px;background:var(--navy);color:#fff;font-family:"Oswald",sans-serif;font-size:14px;display:flex;align-items:center;justify-content:center;clip-path:polygon(0 0,88% 0,100% 50%,88% 100%,0 100%)}
.browse p{padding-left:12px;font-size:9px;line-height:1.5;color:#444}
.browse b{color:var(--blue)}
.panel{position:absolute;top:582px;left:15px;width:637px;height:400px;border:1px solid #d9d9d9;padding:20px 25px}
.cards{display:flex;justify-content:space-between}
.card{width:178px;text-align:center}
.card .pic{height:150px;position:relative;display:flex;align-items:flex-end;justify-content:center;padding-bottom:14px}
.card .pic strong{font-family:"Oswald",sans-serif;font-weight:400;color:#fff;font-size:10px;line-height:1.25;text-shadow:0 1px 2px rgba(0,0,0,.5)}
.card .p1{background:radial-gradient(ellipse 70px 50px at 50% 40%,#2f6fb3 0%,rgba(47,111,179,0) 100%),linear-gradient(#e2e4e7,#3e4349)}
.card .p2{background:radial-gradient(ellipse 45px 60px at 55% 45%,#f1d75a 0%,rgba(241,215,90,0) 100%),linear-gradient(#6fa6d8,#2e5f94)}
.card .p3{background:radial-gradient(ellipse 70px 40px at 50% 45%,#e6dfcf 0%,rgba(230,223,207,0) 100%),linear-gradient(#b8a98a,#3e3830)}
.btn{display:inline-block;margin-top:7px;background:var(--navy);color:#fff;font-size:6.5px;padding:4px 12px}
.form{margin-top:44px;padding-left:52px}
.form h2{font-family:"Oswald",sans-serif;font-weight:600;font-size:17px;color:var(--navy)}
.form p{font-size:8px;margin:3px 0 14px}
.row{display:flex;gap:10px;margin-bottom:10px}
.field{width:108px;height:20px;border:1px solid #ccc;font-size:6px;color:#999;padding:0 5px;line-height:18px}
.field.wide{width:226px}
.send{width:108px;height:20px;background:var(--navy);color:#fff;font-family:"Oswald",sans-serif;font-size:9px;text-align:center;line-height:20px}
.partners{position:absolute;top:992px;left:15px;width:637px;height:40px;border-top:1px solid #ddd;border-bottom:1px solid #ddd;display:flex;align-items:center;justify-content:space-between}
.partners .logos{display:flex;gap:6px}
.partners .logos i{width:66px;height:22px;display:block;border:1px solid #cfd3d8}
.partners .logos i:nth-child(1){background:var(--red)}
.partners .logos i:nth-child(2){background:#fff;border-top:6px solid var(--red)}
.partners .logos i:nth-child(3){background:#e13a1f}
.partners .logos i:nth-child(4){background:#1b3e8c}
.partners .logos i:nth-child(5){background:#fff;border-bottom:6px solid #2e74c6}
.partners .logos i:nth-child(6){background:linear-gradient(90deg,#1e67b5 50%,#fff 50%)}
.partners .logos i:nth-child(7){background:#fff;border-left:14px solid #2a2a2a}
.partners .logos i:nth-child(8){background:#5f6e7e}
.footer{position:absolute;top:1064px;left:0;width:667px;height:136px;background:#3a3d42;display:flex;padding:12px 15px;color:#d3d6da}
.map{width:150px;height:110px;background:radial-gradient(ellipse 22px 45px at 55% 50%,#8a929b 0%,rgba(138,146,155,0) 100%),linear-gradient(#5a636d,#474d55)}
.links{display:flex;gap:28px;margin-left:50px;padding-top:6px}
.links ul{list-style:none}
.links li{font-size:6.5px;line-height:1.75}
.foot-brand{margin-left:auto;text-align:center;width:150px;padding-top:8px}
.foot-brand .brand{color:#fff;font-size:20px;justify-content:center}
.foot-brand small{display:block;font-size:5.5px;margin:6px 0}
.social{display:flex;gap:5px;justify-content:center}
.social i{width:10px;height:10px;border-radius:50%;background:#7b8189;display:block}
</style>
</head>
<body>
<header class="header">
  <div class="brand"><i></i>Vornaspec</div>
  <div class="tagline">Wholesale importer &amp; distributor of quality Italian industrial, commercial &amp; domestic cleaning machines &amp; accessories</div>
  <div class="contact">
    4 / 22 Harlow St, Otaki, Open to the public<br>Head office Otaki Coast | Distributors NZ wide
    <div class="phone"><svg width="14" height="14" viewBox="0 0 24 24"><path fill="#1d2944" d="M6.6 10.8c1.4 2.8 3.8 5.1 6.6 6.6l2.2-2.2c.3-.3.7-.4 1-.2 1.1.4 2.3.6 3.6.6.6 0 1 .4 1 1V20c0 .6-.4 1-1 1C10.6 21 3 13.4 3 4c0-.6.4-1 1-1h3.5c.6 0 1 .4 1 1 0 1.3.2 2.5.6 3.6.1.3 0 .7-.2 1z"/></svg>04 555 0142</div>
  </div>
</header>
<nav class="nav">
  <a class="active">Home</a><a>About</a><a>Water blasters</a><a>Drain cleaners</a><a>Custom machines</a><a>Vacuum Cleaners</a><a>Pumps</a><a>Spare parts</a><a>PTO machines</a><a>FAQ</a><a>Quote</a><a>Contact</a>
</nav>

<section class="hero">
  <div class="hero-photo" role="img" aria-label="Operator using a red hot high pressure washer on a staircase">
    <div class="caption">HOT HIGH PRESSURE WASHER</div>
    <div class="dots"><i></i><i></i><i></i><i></i><i></i></div>
  </div>
  <div class="why">
    <h2>Why Choose Vornaspec?</h2>
    <ul>
      <li>High quality Italian cleaning machines</li>
      <li>Wide range of brands and models</li>
      <li>Specialist knowledge &amp; expert advice</li>
      <li>Cost of machines – more affordable for top quality</li>
      <li>Able to service and repair all types of cleaning machines</li>
      <li>Huge range of affordable spare parts</li>
      <li>Distributors nationwide offering excellent sales &amp; service</li>
      <li>Great family business with excellent customer service for over 14 years</li>
    </ul>
  </div>
</section>

<div class="section-title"><span>HUGE RANGE OF QUALITY CLEANING MACHINES</span></div>
<section class="products">
  <div class="arrow">‹</div>
  <div class="product"><div class="pic" role="img" aria-label="Water blaster machine"></div><span>WATER BLASTERS</span></div>
  <div class="product"><div class="pic" role="img" aria-label="Drain cleaning machine"></div><span>DRAIN CLEANERS</span></div>
  <div class="product"><div class="pic" role="img" aria-label="Drain cleaning machine"></div><span>DRAIN CLEANERS</span></div>
  <div class="product"><div class="pic" role="img" aria-label="Drain cleaning machine"></div><span>DRAIN CLEANERS</span></div>
  <div class="product"><div class="pic" role="img" aria-label="Drain cleaning machine"></div><span>DRAIN CLEANERS</span></div>
  <div class="arrow">›</div>
</section>

<section class="browse">
  <div class="browse-tab">Browse</div>
  <p><b>Products.</b> Add any item to a quote request form or <b>Give us a call</b> for more information.<br>Not sure what you need? <b>Contact us for expert advice – we're happy to assist!</b></p>
</section>

<section class="panel">
  <div class="cards">
    <div class="card"><div class="pic p1" role="img" aria-label="Range of cleaning machines"><strong>HUGE RANGE OF QUALITY<br>CLEANING MACHINES</strong></div><span class="btn">All Products</span></div>
    <div class="card"><div class="pic p2" role="img" aria-label="Map of New Zealand distributors"><strong>NATIONWIDE DISTRIBUTORS<br>FOR SALES &amp; SERVICING</strong></div><span class="btn">Locate</span></div>
    <div class="card"><div class="pic p3" role="img" aria-label="Assorted spare parts"><strong>COMPREHENSIVE RANGE<br>OF SPARE PARTS</strong></div><span class="btn">Spare Parts</span></div>
  </div>
  <div class="form">
    <h2>Would You Like A Vornaspec Representative to Contact You ?</h2>
    <p>Please fill in the form and we'll be in touch very soon...</p>
    <div class="row"><div class="field">First Name</div><div class="field">Last Name</div><div class="field">Contact</div><div class="field">E-mail Address</div></div>
    <div class="row"><div class="field">Enter your interest</div><div class="field wide">Any further details</div><div class="send">SEND ENQUIRY</div></div>
  </div>
</section>

<section class="partners" aria-label="Partner brands">
  <div class="arrow">‹</div>
  <div class="logos"><i></i><i></i><i></i><i></i><i></i><i></i><i></i><i></i></div>
  <div class="arrow">›</div>
</section>

<footer class="footer">
  <div class="map" role="img" aria-label="Map of New Zealand"></div>
  <div class="links">
    <ul><li>Home</li><li>About</li><li>Meet the Team</li><li>Testimonials</li><li>FAQ</li><li>Quote</li><li>Contact/Map</li></ul>
    <ul><li>Water blasters</li><li>Drain cleaners</li><li>Custom machines</li><li>Vacuum Cleaners</li><li>Partial high pressure</li><li>Spare Parts</li><li>PTO machines</li></ul>
  </div>
  <div class="foot-brand">
    <div class="brand">Vornaspec</div>
    <small>© Copyright Vornaspec LTD. 2014. All Rights Reserved.</small>
    <div class="social"><i></i><i></i><i></i></div>
  </div>
</footer>
</body>
</html>
```